Custom Harbor Blinds ( I have a logo)

We need a medium van wrap design (Norvik talora cargo van 2500 regular base 4 doors) for small business. We develop custom windows treatmeants ( blind...

Target Market(s)

Installations and sales of window coverings

Industry/Entity Type

Business

Requirements
Must have
• Clean description of what we do and the slogan of the company ( Your vision, our quality
Nice to have
• Clean and professional look, free consultation , fully insured
Should not have
• To many pictures, we are more interested on customers focusing in what kind of work we perform than looking an a gallery on wheels

```html
<!DOCTYPE html>
<html lang="en">
<head>
<meta charset="utf-8">
<title>Custom Harbor Blinds – Van Wrap</title>
<link href="https://fonts.googleapis.com/css2?family=Roboto+Condensed:wght@400;700&display=swap" rel="stylesheet">
<style>
  :root {
    --orange: #f26a36;
    --ink: #1d1d1d;
    --paper: #ffffff;
    --panel-line: #d9d9d9;
  }
  html, body { margin: 0; padding: 0; overflow: hidden; }
  body { background: var(--paper); }
  .wrap {
    position: relative; width: 1200px; height: 797px; overflow: hidden;
    background: var(--paper); font-family: "Roboto Condensed", sans-serif; color: var(--ink);
  }
  .panel {
    position: absolute; left: 528px; top: 208px; width: 522px; height: 108px;
    border: 1px solid var(--panel-line); border-radius: 8px;
  }
  .panel-divider {
    position: absolute; left: 772px; top: 210px; width: 1px; height: 104px; background: var(--panel-line);
  }
  .brand {
    position: absolute; display: flex; flex-direction: column; align-items: center; gap: 8px;
    text-align: center;
  }
  .brand-dot { width: 18px; height: 18px; border-radius: 50%; background: var(--orange); }
  .brand-name { font-weight: 700; color: var(--ink); line-height: 1; white-space: nowrap; }
  .brand--panel { left: 553px; width: 200px; top: 226px; }
  .brand--panel .brand-name { font-size: 24px; }
  .brand--door { left: 336px; width: 154px; top: 380px; }
  .brand--door .brand-name { font-size: 19px; }
  .tagline { position: absolute; left: 553px; width: 200px; text-align: center; top: 289px; font-size: 13px; font-weight: 700; }
  .services { position: absolute; left: 800px; top: 219px; margin: 0; padding: 0; list-style: none; }
  .services li { display: flex; align-items: center; gap: 6px; font-size: 12.5px; font-weight: 700; line-height: 16px; }
  .services svg { width: 12px; height: 12px; }
  .headline {
    position: absolute; left: 540px; top: 326px; width: 510px; text-align: center;
    color: var(--orange); font-weight: 700; font-size: 16.5px; line-height: 21px;
    transform: rotate(-1.4deg);
  }
  .call { position: absolute; left: 336px; top: 441px; font-size: 18px; font-weight: 700; letter-spacing: .3px; }
  .url { color: var(--orange); font-weight: 700; white-space: nowrap; }
  .url--door { position: absolute; left: 335px; top: 460px; font-size: 12.5px; }
  .swoosh { position: absolute; left: 0; top: 0; }
  .tilted { position: absolute; transform-origin: left top; font-weight: 700; line-height: 1; white-space: nowrap; }
  .offer-title { left: 530px; top: 452px; font-size: 21px; transform: rotate(-9deg); }
  .offer-title .free { color: var(--orange); }
  .offer-phone { left: 632px; top: 455px; font-size: 32px; letter-spacing: .5px; transform: rotate(-9deg); }
  .offer-url { left: 642px; top: 479px; font-size: 12px; transform: rotate(-8deg); }
</style>
</head>
<body>
<div class="wrap">
  <div class="panel"></div>
  <div class="panel-divider"></div>

  <div class="brand brand--panel">
    <div class="brand-dot"></div>
    <div class="brand-name">Custom Harbor Blinds</div>
  </div>
  <div class="tagline">Your vision, our quality</div>

  <ul class="services">
    <li><svg viewBox="0 0 12 12"><path d="M1 6.5 4.5 10 11 1.5" fill="none" stroke="#f26a36" stroke-width="2.4"/></svg>WINDOW TREATMENTS</li>
    <li><svg viewBox="0 0 12 12"><path d="M1 6.5 4.5 10 11 1.5" fill="none" stroke="#f26a36" stroke-width="2.4"/></svg>CUSTOM SHADES</li>
    <li><svg viewBox="0 0 12 12"><path d="M1 6.5 4.5 10 11 1.5" fill="none" stroke="#f26a36" stroke-width="2.4"/></svg>ROMAN SHADES</li>
    <li><svg viewBox="0 0 12 12"><path d="M1 6.5 4.5 10 11 1.5" fill="none" stroke="#f26a36" stroke-width="2.4"/></svg>UPHOLSTERY SERVICES</li>
    <li><svg viewBox="0 0 12 12"><path d="M1 6.5 4.5 10 11 1.5" fill="none" stroke="#f26a36" stroke-width="2.4"/></svg>AWNINGS</li>
  </ul>

  <div class="headline">We Custom Make, Distribute and Install Modern Window Treatments<br>You'll Absolutely Love</div>

  <svg class="swoosh" width="1200" height="797" viewBox="0 0 1200 797" aria-hidden="true">
    <polygon points="512,398 790,388 512,416" fill="var(--orange)"/>
    <polygon points="512,424 1074,362 512,455" fill="var(--orange)"/>
  </svg>

  <div class="brand brand--door">
    <div class="brand-dot"></div>
    <div class="brand-name">Custom Harbor Blinds</div>
  </div>
  <div class="call">CALL 555-014-2276</div>
  <div class="url url--door">www.customharborblinds.com</div>

  <div class="tilted offer-title"><span class="free">FREE</span> CONSULTATION &amp; ESTIMATE</div>
  <div class="tilted offer-phone">555-014-2276</div>
  <div class="tilted offer-url url">www.customharborblinds.com</div>
</div>
</body>
</html>
```